Womans Supplement Designs

Launching a Supplement company and need to get some initial designs created, I've attached our logo and the bottle type that I want the samples done one.

This project is for our Whey Protein we are starting with Vanilla, chocolate and strawberry banana

(ALL DESIGN VARIATIONS MUST BE A WHITE BOTTLE NOT BLACK)

(FOR DESIGN SAMPLES PLEASE USE THE SUPPLEMENT BOTTLE STYLE I PROVIDED)

Whoever is selected the winner I will have more work for you to complete the disigns for the rest of the products in the line, Just want to get this shake completed first

Women

• Must have our current logo involved

the name of this product will be "BLUE OAK"

Must have this slogan,

ALL-IN-ONE PREMIUM PROTEIN NUTRITIONAL SHAKE FOR BLACK WOMEN

This is our meal replacement

the design should try to keep the same look and feel of the existing provided supplement images

we are starting with chocolate, vanilla and strawberry banana

this is for women and should look colorful and appeal to them
• Do not use an image of a person or lady, don't want it branded to a person

```html
<!DOCTYPE html>
<html lang="en">
<head>
<meta charset="utf-8">
<title>Blue Oak – Vanilla Protein Shake Label</title>
<link href="https://fonts.googleapis.com/css2?family=Barlow:wght@400;500;600&display=swap" rel="stylesheet">
<style>
  :root {
    --page: #ffffff;
    --label-pink: #e9958a;
    --label-pink-light: #f3aaa1;
    --ink: #262626;
    --ink-soft: #4a3b39;
    --flavor-mint: #b9e7df;
    --ornament: #f0a69d;
  }
  * { margin: 0; padding: 0; box-sizing: border-box; }
  html, body {
    width: 1200px;
    height: 1200px;
    overflow: hidden;
    background: var(--page);
    font-family: "Barlow", sans-serif;
  }
  .canvas {
    position: relative;
    width: 1200px;
    height: 1200px;
  }
  .label {
    position: absolute;
    left: 95px;
    top: 180px;
    width: 1010px;
    height: 840px;
    background: linear-gradient(90deg, var(--label-pink-light) 0%, var(--label-pink) 45%, var(--label-pink) 80%, var(--label-pink-light) 100%);
    overflow: hidden;
  }
  .label__ornament {
    position: absolute;
    left: 696px;
    top: 30px;
    width: 314px;
    height: 780px;
    background: var(--ornament);
    opacity: 0.6;
  }
  .brand {
    position: absolute;
    left: 81px;
    top: 118px;
    display: flex;
    align-items: center;
    gap: 14px;
    color: var(--ink);
    font-size: 40px;
    font-weight: 500;
    letter-spacing: 2px;
    line-height: 1;
  }
  .brand__mark {
    width: 22px;
    height: 22px;
    background: var(--ink);
  }
  .product-name {
    position: absolute;
    left: 74px;
    top: 262px;
    font-size: 152px;
    font-weight: 600;
    line-height: 1;
    letter-spacing: -2px;
    color: var(--ink);
    text-transform: lowercase;
  }
  .slogan {
    position: absolute;
    left: 81px;
    top: 478px;
    font-size: 23px;
    font-weight: 500;
    line-height: 36px;
    letter-spacing: 1px;
    color: var(--ink-soft);
    text-transform: uppercase;
  }
  .slogan__audience { color: var(--ink); font-weight: 600; }
  .flavor {
    position: absolute;
    left: 0;
    top: 651px;
    width: 345px;
    height: 99px;
    background: var(--flavor-mint);
    border-radius: 0 10px 10px 0;
    display: flex;
    align-items: center;
    padding-left: 81px;
    font-size: 21px;
    font-weight: 500;
    letter-spacing: 1px;
    color: var(--ink-soft);
    text-transform: uppercase;
  }
  .net-weight {
    position: absolute;
    left: 81px;
    top: 776px;
    font-size: 21px;
    font-weight: 500;
    letter-spacing: 1px;
    color: var(--ink-soft);
    text-transform: uppercase;
  }
</style>
</head>
<body>
<main class="canvas">
  <section class="label">
    <div class="label__ornament" role="img" aria-label="White geometric chevron line pattern on the right side of the label"></div>
    <p class="brand"><span class="brand__mark"></span>EMBER GRACE</p>
    <h1 class="product-name">BLUE OAK</h1>
    <p class="slogan">
      All-in-one premium protein<br>
      Nutritional shake<br>
      <span class="slogan__audience">For black women</span>
    </p>
    <p class="flavor">Vanilla flavor</p>
    <p class="net-weight">Net wt 500g</p>
  </section>
</main>
</body>
</html>
```